Hvac and insulation company needs good looking business card design

We are hvac and insulation company and looking for a new business cards that look to today standards designs

Target Market(s)

homeowners

Industry/Entity Type

Hvac

Contact Information for Business Card

Name: Dorian Velkova
Home comfort consultant
address: 4827 Marrow Ridge Rd #215 Oakland, CA 94611
office: 888-317-5069
cell: 510-642-1388
Lic.# 458127
Email: dorian@quarry-hvac.com
Web: quarry-hvac.com

Requirements
Must have
• clean and sleek look
Nice to have
• simple with a clean look
Should not have
• to busy business card

```html
<!DOCTYPE html>
<html lang="en">
<head>
<meta charset="utf-8">
<title>Quarry – Business Card</title>
<link rel="stylesheet" href="https://fonts.googleapis.com/css2?family=Barlow+Semi+Condensed:wght@400;500;600&display=swap">
<style>
  :root {
    --stage: #4a4a4c;
    --card: #ffffff;
    --brand-orange: #f28a36;
    --name-blue: #1aa3df;
    --ink: #555658;
    --rule: #4f5052;
    --grey-deep: #8a8a8c;
    --grey-mid: #cfcfd0;
    --grey-soft: #ececec;
    --orange-deep: #f08532;
    --yellow: #ffcb2e;
    --peach: #fbdcc4;
  }
  html, body {
    margin: 0;
    padding: 0;
    width: 1200px;
    height: 1000px;
    overflow: hidden;
    background: var(--stage);
    font-family: "Barlow Semi Condensed", "Arial Narrow", sans-serif;
  }
  .stage {
    position: relative;
    width: 1200px;
    height: 1000px;
  }
  .card {
    position: absolute;
    left: 275px;
    width: 653px;
    height: 408px;
    background: var(--card);
    overflow: hidden;
  }
  .card--front { top: 85px; }
  .card--back { top: 509px; height: 407px; }

  /* decorative artwork areas */
  .art {
    position: absolute;
    display: block;
  }
  .art--front-corner {
    left: 0;
    bottom: 0;
    width: 600px;
    height: 235px;
    background: linear-gradient(20deg, var(--grey-deep) 0%, var(--grey-mid) 30%, var(--grey-soft) 55%, rgba(255,255,255,0) 80%);
  }
  .art--front-top {
    right: 0;
    top: 0;
    width: 260px;
    height: 92px;
    background: linear-gradient(200deg, var(--grey-mid) 0%, var(--grey-soft) 35%, rgba(255,255,255,0) 75%);
  }
  .art--back-top {
    left: 0;
    top: 0;
    width: 215px;
    height: 90px;
    background: linear-gradient(160deg, #fcd39f 0%, #fff0dc 40%, rgba(255,255,255,0) 80%);
  }
  .art--back-corner {
    right: 0;
    bottom: 0;
    width: 600px;
    height: 235px;
    background: linear-gradient(160deg, rgba(255,255,255,0) 35%, var(--peach) 55%, var(--yellow) 78%, var(--orange-deep) 100%);
  }

  .brand {
    position: absolute;
    left: 213px;
    top: 148px;
    display: flex;
    align-items: center;
    gap: 22px;
  }
  .brand__mark {
    width: 62px;
    height: 62px;
    background: var(--brand-orange);
  }
  .brand__name {
    font-size: 84px;
    font-weight: 500;
    line-height: 1;
    color: var(--brand-orange);
    letter-spacing: 1px;
  }
  .license {
    position: absolute;
    right: 20px;
    top: 20px;
    margin: 0;
    font-size: 19px;
    font-weight: 600;
    line-height: 1;
    color: var(--ink);
  }
  .person {
    position: absolute;
    left: 122px;
    top: 72px;
  }
  .person__name {
    margin: 0;
    font-size: 38px;
    font-weight: 400;
    line-height: 1;
    color: var(--name-blue);
    letter-spacing: 0.4px;
  }
  .person__name strong { font-weight: 600; }
  .person__title {
    margin: 8px 0 0;
    font-size: 21px;
    line-height: 1.1;
    color: var(--ink);
  }
  .person__rule {
    width: 222px;
    height: 2px;
    margin: 18px 0 0;
    background: var(--rule);
    border: 0;
  }
  .contacts {
    position: absolute;
    left: 98px;
    top: 175px;
    margin: 0;
    padding: 0;
    list-style: none;
    font-size: 19.5px;
    color: var(--ink);
    line-height: 29px;
  }
  .contacts li {
    display: flex;
    align-items: center;
    gap: 9px;
  }
  .contacts .gap-top { margin-top: 29px; }
  .contacts .icon {
    width: 15px;
    height: 15px;
    flex: none;
  }
  .contacts .no-icon { padding-left: 24px; }
</style>
</head>
<body>
<main class="stage">

  <section class="card card--front" aria-label="Card front">
    <span class="art art--front-top" role="img" aria-label="Grey faceted decorative artwork in the top corner"></span>
    <span class="art art--front-corner" role="img" aria-label="Grey faceted decorative artwork along the lower left"></span>
    <div class="brand">
      <span class="brand__mark"></span>
      <span class="brand__name">quarry</span>
    </div>
  </section>

  <section class="card card--back" aria-label="Card back">
    <span class="art art--back-top" role="img" aria-label="Warm yellow and peach faceted decorative artwork in the top corner"></span>
    <span class="art art--back-corner" role="img" aria-label="Orange, yellow and peach faceted decorative artwork along the lower right"></span>

    <p class="license">Lic.# 458127</p>

    <div class="person">
      <h1 class="person__name">DORIAN <strong>VELKOVA</strong></h1>
      <p class="person__title">Home comfort consultant</p>
      <hr class="person__rule">
    </div>

    <ul class="contacts">
      <li>
        <svg class="icon" viewBox="0 0 16 16" aria-hidden="true"><path d="M8 1a5 5 0 0 0-5 5c0 3.6 5 9 5 9s5-5.4 5-9a5 5 0 0 0-5-5zm0 7a2 2 0 1 1 0-4 2 2 0 0 1 0 4z" fill="#555658"/></svg>
        4827 Marrow Ridge Rd #215 Oakland, CA 94611
      </li>
      <li>
        <svg class="icon" viewBox="0 0 16 16" aria-hidden="true"><path d="M4 1.5 6.2 4 5 6c.8 2 2.5 3.8 5 5l2-1.2 2.5 2.2-1.6 2.3C8 14 2 8 1.8 3z" fill="none" stroke="#555658" stroke-width="1.5" stroke-linejoin="round"/></svg>
        888-317-5069
      </li>
      <li class="no-icon">510-642-1388</li>
      <li class="gap-top">
        <svg class="icon" viewBox="0 0 16 16" aria-hidden="true"><rect x="2" y="4" width="12" height="8.5" fill="none" stroke="#555658" stroke-width="1.2"/><path d="M2 4l6 5 6-5" fill="none" stroke="#555658" stroke-width="1.2"/></svg>
        dorian@quarry-hvac.com
      </li>
      <li>
        <svg class="icon" viewBox="0 0 16 16" aria-hidden="true"><g fill="none" stroke="#555658" stroke-width="1.2"><circle cx="8" cy="8" r="6.2"/><ellipse cx="8" cy="8" rx="2.8" ry="6.2"/><path d="M1.8 8h12.4"/></g></svg>
        quarry-hvac.com
      </li>
    </ul>
  </section>

</main>
</body>
</html>
```